Night Dresses business cards business requirers

We are a new company initiating Mexico operations. Our core business is Night woman dress (both formal and party dress) for rent. Gownhaven is the name of the company. ITS Gownhaven form by two word. The dress word and topia (Utopic) so the place Gownhaven Means That You cant get the ideal, perfect and unique dress for your event. So we would like a modern, very creative, and attractive business card.

Industry/Entity Type

Womens Clothing

Contact Information for Business Card

Rounded Borders, two faces

Requirements
Must have
• Rounded borders, logo and slogan, modern, glam, attractive design
Should not have
• modern design classic or not

```html
<!DOCTYPE html>
<html lang="en">
<head>
<meta charset="utf-8">
<title>Gownhaven Business Cards</title>
<link href="https://fonts.googleapis.com/css2?family=Ubuntu:wght@400;500;700&display=swap" rel="stylesheet">
<style>
  :root {
    --stage: #1a1a1a;
    --card: #ffffff;
    --card-back: #f7f7f7;
    --orchid: #b5628f;
    --ink: #3a3a3a;
    --white: #ffffff;
  }
  * { margin: 0; padding: 0; box-sizing: border-box; }
  html, body {
    width: 1200px; height: 900px; overflow: hidden;
    background: var(--stage);
    font-family: "Ubuntu", sans-serif;
  }
  .stage { position: relative; width: 1200px; height: 900px; }
  .card {
    position: absolute; top: 271px; width: 456px; height: 281px;
    border-radius: 12px; overflow: hidden;
    box-shadow: 3px 4px 6px rgba(0,0,0,0.45);
  }
  .card--front { left: 137px; background: var(--card); }
  .card--back { left: 627px; background: var(--card-back); }
  .card__art { position: absolute; inset: 0; }

  .brand-name {
    position: absolute; color: var(--orchid);
    font-weight: 400; line-height: 1; white-space: nowrap;
  }
  .card--front .brand-name {
    left: 27px; top: 40px; font-size: 21px; letter-spacing: 7px;
  }

  .address {
    position: absolute; right: 26px; top: 31px; text-align: right;
    color: var(--ink); font-size: 13px; line-height: 17px; font-style: normal;
  }

  .holder { position: absolute; left: 27px; top: 138px; color: var(--white); }
  .holder__name { font-size: 20px; font-weight: 700; line-height: 22px; }
  .holder__role { font-size: 12px; font-weight: 400; margin-top: 1px; }

  .contacts {
    position: absolute; left: 27px; top: 194px; list-style: none;
    color: var(--white); font-size: 13px; line-height: 17.5px;
  }
  .contacts li { display: flex; align-items: center; gap: 6px; }
  .contacts svg { width: 11px; height: 11px; flex: none; }

  .card--back .brand-name {
    left: 0; right: 0; top: 176px; text-align: center;
    font-size: 22px; letter-spacing: 8px; color: var(--ink);
  }
</style>
</head>
<body>
<main class="stage">

  <section class="card card--front" aria-label="Business card front">
    <svg class="card__art" width="456" height="281" viewBox="0 0 456 281" aria-hidden="true">
      <rect class="band" x="0" y="126" width="340" height="130" fill="var(--orchid)"/>
      <circle class="band-cutout" cx="360" cy="191" r="75" fill="var(--card)"/>
      <circle class="emblem-ring" cx="360" cy="191" r="63" fill="none" stroke="var(--orchid)" stroke-width="4"/>
    </svg>

    <div class="brand-name">GOWNHAVEN</div>

    <address class="address">
      2870 Alameda Street<br>Ridgefield, 04510 Mexico
    </address>

    <div class="holder">
      <div class="holder__name">MARA VELASCO</div>
      <div class="holder__role">PRESIDENT</div>
    </div>

    <ul class="contacts">
      <li>
        <svg viewBox="0 0 12 12" aria-hidden="true"><path d="M1 4.5C1 2.5 3.5 1.5 6 1.5S11 2.5 11 4.5L9 5 8.5 3.8h-5L3 5z M3 6h6l1.5 4.5h-9z" fill="var(--white)"/></svg>
        415- 290-7734
      </li>
      <li>
        <svg viewBox="0 0 12 12" aria-hidden="true"><rect x="1" y="2.5" width="10" height="7" fill="var(--white)"/><path d="M1 2.5l5 4 5-4" fill="none" stroke="var(--orchid)" stroke-width="1"/></svg>
        hello@gownhaven.mx
      </li>
      <li>
        <svg viewBox="0 0 12 12" aria-hidden="true"><circle cx="6" cy="6" r="5" fill="var(--white)"/><path d="M3.5 4.5c1 0 1.5 1 2.5 1s.5 2 1.5 2.5M7.5 2.5c-.5 1 .5 1.5 1.5 1.5" fill="none" stroke="var(--orchid)" stroke-width="1"/></svg>
        www.gownhaven.mx
      </li>
    </ul>
  </section>

  <section class="card card--back" aria-label="Business card back">
    <svg class="card__art" width="456" height="281" viewBox="0 0 456 281" aria-hidden="true">
      <rect class="edge-band" x="0" y="0" width="456" height="14" fill="var(--orchid)"/>
      <rect class="edge-band" x="0" y="266" width="456" height="15" fill="var(--orchid)"/>
      <circle class="emblem-ring" cx="226" cy="116" r="44" fill="none" stroke="var(--orchid)" stroke-width="3"/>
    </svg>
    <div class="brand-name">GOWNHAVEN</div>
  </section>

</main>
</body>
</html>
```